Event Graphics for a Summer Camp for Middle School and High School Students

I need graphics designed for our summer camps event. These camps are for teenagers, 6-12th grades. Primary graphic design is for a 11x17 poster but will also need the images resized for:
-social media
-16x9 title slide
- a postcard size
Graphic should include the following:
-Main Title: RV Pathlight presents . . . Summer Camp
-Dates: Kindle - June 3-7, High School - June 8-12, Middle School - June 22-26
-Register at RVPathlight.com
-Maple Crest Retreat Center, Deadwood, SD
-For each camp, include name and headshot of speaker: Kindle: Tom Wakeley (black jacket photo), High: Luis Ortega (hispanic man), Middle: Barrington Pope (tan shirt). Gave some options for headshots. Use what works best for cropping.
-Include RV Pathlight logo
-Event Graphic should be attractive to teenagers. Open to ideas
My graphic design experience is limited. I will need help receiving the files I need in the various sizes. Thank you.

```html
<!DOCTYPE html>
<html lang="en">
<head>
<meta charset="utf-8">
<title>RV Pathlight Summer Camp Poster</title>
<link rel="stylesheet" href="https://fonts.googleapis.com/css2?family=Baloo+2:wght@800&family=Fredoka:wght@600&family=Roboto:wght@400&family=Roboto+Condensed:wght@400&display=swap">
<style>
  :root {
    --page-bg: #e7e4ec;
    --sky: #eef5fa;
    --sky-ray: #cfe3f1;
    --grass-light: #7cc142;
    --grass-dark: #3f8a22;
    --sun: #fff200;
    --sun-edge: #ece000;
    --pink: #ef177a;
    --pink-side: #a3104f;
    --blue: #0c6c9c;
    --blue-side: #08496e;
    --green: #5cbc3c;
    --green-side: #0c7a36;
    --june-yellow: #fff200;
    --navy: #1d2f8c;
    --plum: #6b1a6e;
    --maroon: #9a1552;
    --teal: #10a09c;
    --magenta: #c23a9e;
    --orange: #f35a19;
    --lime: #4fb32f;
    --speaker-blue: #1b6fa8;
    --white: #ffffff;
  }
  html, body {
    margin: 0;
    width: 1040px;
    height: 1200px;
    overflow: hidden;
    background: var(--page-bg);
  }
  .poster {
    position: absolute;
    left: 133px;
    top: 20px;
    width: 774px;
    height: 1160px;
    overflow: hidden;
    background: radial-gradient(circle at 50% 38%, var(--sky) 0%, var(--sky-ray) 100%);
  }
  .poster-art {
    position: absolute;
    inset: 0;
  }
  .box-label {
    font-family: "Baloo 2", sans-serif;
    font-weight: 800;
    text-anchor: middle;
  }
  .box-title { fill: var(--white); font-size: 28px; }
  .box-date { fill: var(--june-yellow); font-size: 33px; }
  .brand-name {
    font-family: "Fredoka", sans-serif;
    font-weight: 600;
    font-size: 34px;
    fill: var(--navy);
    text-anchor: middle;
  }
  .presents {
    font-family: "Fredoka", sans-serif;
    font-weight: 600;
    font-size: 28px;
    fill: var(--plum);
  }
  .headline {
    font-family: "Fredoka", sans-serif;
    font-weight: 600;
    stroke: var(--white);
    stroke-linejoin: round;
    paint-order: stroke;
  }
  .register {
    font-family: "Roboto Condensed", sans-serif;
    font-size: 27px;
    fill: var(--white);
    text-anchor: middle;
  }
  .photo-cloud {
    position: absolute;
    border: 4px solid var(--white);
    border-radius: 46% 54% 50% 50% / 52% 48% 52% 48%;
    background: linear-gradient(180deg, #8cc4ec 0%, #cfe6f6 45%, #6fb23c 70%, #3e8a22 100%);
    box-sizing: border-box;
  }
  .photo-cloud.left { left: 39px; top: 561px; width: 188px; height: 190px; }
  .photo-cloud.right { left: 530px; top: 555px; width: 206px; height: 208px; }
  .speakers-heading {
    position: absolute;
    left: 0;
    width: 774px;
    top: 820px;
    margin: 0;
    text-align: center;
    font-family: "Fredoka", sans-serif;
    font-weight: 600;
    font-size: 28px;
    line-height: 36px;
    color: var(--speaker-blue);
    text-shadow: 0 0 2px var(--white), 0 0 2px var(--white), 0 0 2px var(--white);
  }
  .speaker {
    position: absolute;
    top: 876px;
    width: 200px;
    margin-left: -100px;
    text-align: center;
  }
  .speaker-photo {
    width: 118px;
    height: 118px;
    margin: 0 auto;
    border-radius: 50%;
    border: 3px solid var(--white);
    box-sizing: border-box;
    background: radial-gradient(circle at 50% 40%, #b89a86 0%, #5b4a44 60%, #2a2422 100%);
  }
  .speaker-name {
    margin: 16px 0 0;
    font-family: "Roboto", sans-serif;
    font-size: 16px;
    color: var(--white);
    white-space: nowrap;
  }
  .speaker.high { left: 168px; }
  .speaker.middle { left: 381px; }
  .speaker.kindle { left: 583px; }
  .venue-bar {
    position: absolute;
    left: 77px;
    top: 1064px;
    width: 621px;
    height: 72px;
    border-radius: 36px;
    background: var(--sun);
    display: flex;
    align-items: center;
    justify-content: center;
    font-family: "Roboto Condensed", sans-serif;
    font-size: 28px;
    color: var(--plum);
  }
  .venue-dot {
    position: absolute;
    top: 20px;
    width: 32px;
    height: 32px;
    border-radius: 50%;
    background: var(--magenta);
  }
  .venue-dot.start { left: 12px; }
  .venue-dot.end { right: 12px; }
</style>
</head>
<body>
<main class="poster">
  <svg class="poster-art" width="774" height="1160" viewBox="0 0 774 1160">
    <defs>
      <linearGradient id="grass-fill" x1="0" y1="0" x2="0" y2="1">
        <stop offset="0" stop-color="var(--grass-light)"/>
        <stop offset="1" stop-color="var(--grass-dark)"/>
      </linearGradient>
    </defs>
    <path d="M0,595 Q387,458 774,497 L774,1160 L0,1160 Z" fill="var(--white)"/>
    <path d="M0,605 Q387,470 774,507 L774,1160 L0,1160 Z" fill="url(#grass-fill)" role="img" aria-label="Photograph of a green grass field"/>

    <g class="date-box high-school">
      <polygon points="32,280 218,268 240,292 125,372" fill="var(--pink-side)"/>
      <g transform="rotate(-4 121 200)">
        <rect x="27" y="116" width="188" height="168" rx="8" fill="var(--pink)"/>
        <text class="box-label box-title" x="121" y="162">High School</text>
        <text class="box-label box-date" x="112" y="202">June</text>
        <text class="box-label box-date" x="112" y="240">8 - 12</text>
      </g>
    </g>
    <g class="date-box kindle">
      <polygon points="445,30 480,70 500,170 470,210 300,214" fill="var(--blue-side)"/>
      <g transform="rotate(-5 361 108)">
        <rect x="267" y="21" width="188" height="173" rx="8" fill="var(--blue)"/>
        <text class="box-label box-title" x="361" y="72">KINDLE</text>
        <text class="box-label box-date" x="361" y="112">June</text>
        <text class="box-label box-date" x="361" y="150">3-7</text>
      </g>
    </g>
    <g class="date-box middle-school">
      <polygon points="530,250 705,262 680,300 640,340 600,330" fill="var(--green-side)"/>
      <g transform="rotate(5 619 180)">
        <rect x="529" y="96" width="180" height="169" rx="8" fill="var(--green)"/>
        <text class="box-label box-title" x="619" y="138" style="font-size:25px">Middle School</text>
        <text class="box-label box-date" x="619" y="176">June</text>
        <text class="box-label box-date" x="619" y="214">22 - 26</text>
      </g>
    </g>

    <g class="sun">
      <circle cx="392" cy="218" r="42" fill="var(--sun-edge)"/>
      <circle cx="290" cy="252" r="44" fill="var(--sun-edge)"/>
      <circle cx="496" cy="255" r="44" fill="var(--sun-edge)"/>
      <circle cx="588" cy="335" r="44" fill="var(--sun-edge)"/>
      <circle cx="630" cy="432" r="40" fill="var(--sun-edge)"/>
      <circle cx="636" cy="528" r="36" fill="var(--sun-edge)"/>
      <circle cx="196" cy="335" r="44" fill="var(--sun-edge)"/>
      <circle cx="152" cy="432" r="40" fill="var(--sun-edge)"/>
      <circle cx="148" cy="528" r="36" fill="var(--sun-edge)"/>
      <circle cx="392" cy="442" r="236" fill="var(--sun)"/>
    </g>

    <text class="brand-name" x="386" y="264">RV Pathlight</text>
    <text class="presents" x="341" y="338" transform="rotate(-6 341 338)">presents</text>
    <text class="headline" x="238" y="462" font-size="96" stroke-width="10" transform="rotate(-10 238 462)"><tspan fill="var(--blue)">S</tspan><tspan fill="var(--teal)">u</tspan><tspan fill="var(--lime)">m</tspan><tspan fill="var(--lime)">m</tspan><tspan fill="var(--pink)">e</tspan><tspan fill="var(--orange)">r</tspan></text>
    <text class="headline" x="186" y="606" font-size="170" stroke-width="12" transform="rotate(-8 186 606)"><tspan fill="var(--maroon)">C</tspan><tspan fill="var(--teal)">a</tspan><tspan fill="var(--magenta)">m</tspan><tspan fill="var(--orange)">p</tspan></text>

    <path d="M204,688 Q390,650 569,700 L569,758 Q390,712 204,746 Z" fill="var(--maroon)"/>
    <text class="register" x="386" y="726" transform="rotate(4 386 716)">Register at RVPathlight.com</text>
  </svg>

  <div class="photo-cloud left" role="img" aria-label="Photo of children running across a grassy field"></div>
  <div class="photo-cloud right" role="img" aria-label="Photo of children running with a rainbow kite"></div>

  <h2 class="speakers-heading">Speakers:</h2>
  <div class="speaker high">
    <div class="speaker-photo" role="img" aria-label="Headshot of speaker Luis Ortega"></div>
    <p class="speaker-name">High: Luis Ortega</p>
  </div>
  <div class="speaker middle">
    <div class="speaker-photo" role="img" aria-label="Headshot of speaker Barrington Pope"></div>
    <p class="speaker-name">Middle: Barrington Pope</p>
  </div>
  <div class="speaker kindle">
    <div class="speaker-photo" role="img" aria-label="Headshot of speaker Tom Wakeley"></div>
    <p class="speaker-name">Kindle: Tom Wakeley</p>
  </div>

  <div class="venue-bar">
    <span class="venue-dot start"></span>
    Maple Crest Retreat Center, Deadwood, SD
    <span class="venue-dot end"></span>
  </div>
</main>
</body>
</html>
```